CareWillow Brand Standards and Core Values

I would like to have frameable posters made up for each office using our brand standards. I would like the posters to include:Our Vision Statement:We are transforming the healthcare staffing and homecare industry with our people-oriented, world-class team. Clients choose us, and develop lasting bonds with our team because of our impeccably high standards and our reputation for always remembering this is, first and foremost, a people business. We consistently go the extra mile to ensure our nurses and those being cared for are at all times, treated with dignity and respect. We hold ourselves and those we work with to the highest possible standards. We consistently deliver what we promise, and whenever possible, even more. Our Mission Statement:We go above and beyond to ensure our clients receive the right care and the right people at the right time. Our rigorous recruitment standards result in strong caregivers who are trusted for their expertise, experience and compassion. Our Values:Through our genuine caring and compassion, we are committed to honor all with whom we interact. We are grounded in our faith and dedicated to working together as a family that consistently and passionately lives our values. Compassion Integrity and honesty Faith Decisive action Constant and never-ending improvement Personal ownership Excellence Positive attitude Passion RespectWho we are:We are friendly, servant leaders who have a sense of urgency to meet the needs of our nurses and clients. We prioritize personal relationships with genuine caring and compassion. We inspire others through our passion and energy.Our main colors are: HEX# 5C80DE, HEX# BDE080, HEX# 8C8C8Caccent colors are: HEX# 95D6E3, HEX# AD59AB, HEX# 002E57

Target Market(s)

office employee inspiration

Font styles to use
Other font styles liked:
• Verdana

Colors

Designer to choose colors to be used in the design.

Requirements
Must have
• the core values listed in description
Nice to have
• colors given in description, something fun and inspiring for office employees to help motivate them !
Should not have
• colors that are not company colors. I have listed HEX codes in description

```html
<!DOCTYPE html>
<html lang="en">
<head>
<meta charset="utf-8">
<title>CareWillow Core Values Poster</title>
<link rel="stylesheet" href="https://fonts.googleapis.com/css2?family=Open+Sans:wght@400;600&family=Saira+Condensed:wght@600;700&display=swap">
<style>
  :root {
    --backdrop: #ececec;
    --paper: #ffffff;
    --brand-green: #bde080;
    --brand-navy: #002e57;
    --brand-blue: #5c80de;
    --ink: #1a1a1a;
    --band-grey: #ebebed;
    --panel-dark: #3d3d3e;
    --panel-mid: #555556;
    --panel-text: #ffffff;
    --footer: #000000;
  }
  * { box-sizing: border-box; margin: 0; padding: 0; }
  html, body {
    width: 1200px; height: 960px; overflow: hidden;
    background: var(--backdrop);
  }
  .poster {
    position: absolute; left: 288px; top: 20px;
    width: 623px; height: 920px;
    background: var(--paper);
    box-shadow: 0 6px 18px rgba(0,0,0,0.18);
    font-family: "Open Sans", Verdana, sans-serif;
    display: flex; flex-direction: column;
  }
  .brand-bar {
    height: 64px; display: flex; align-items: center; justify-content: center; gap: 10px;
  }
  .brand-mark {
    width: 22px; height: 22px; border-radius: 50%; background: var(--brand-blue);
  }
  .brand-name {
    font-family: "Open Sans", Verdana, sans-serif; font-weight: 600;
    font-size: 20px; color: var(--brand-navy); letter-spacing: 0.2px;
  }
  .hero { height: 351px; display: flex; }
  .hero-photo {
    width: 312px; height: 100%;
    background: linear-gradient(160deg, #b9b9b9 0%, #8a8a8a 40%, #2c3546 75%, #1e2534 100%);
  }
  .hero-message {
    flex: 1; background: var(--brand-green); padding: 24px 22px 0 29px;
  }
  .hero-headline {
    font-family: "Saira Condensed", "Arial Narrow", sans-serif; font-weight: 700;
    font-size: 39px; line-height: 37px; color: var(--brand-navy); letter-spacing: 0.3px;
  }
  .hero-copy {
    margin-top: 16px; font-size: 14.6px; line-height: 20.2px; color: var(--ink);
  }
  .promise-band {
    height: 107px; background: var(--band-grey);
    display: flex; align-items: center; justify-content: center;
    padding: 0 24px 10px; text-align: center;
    font-size: 13.8px; line-height: 19px; color: var(--ink);
    border-bottom: 2px solid #d4d4d6;
  }
  .statement-grid {
    display: grid; grid-template-columns: 312px 1fr; grid-template-rows: 160px 202px;
    background: linear-gradient(180deg, var(--panel-dark) 0%, var(--panel-mid) 100%);
    color: var(--panel-text);
  }
  .statement { padding: 8px 20px 0 24px; }
  .statement.right { padding-left: 16px; }
  .statement.lower { background: rgba(255,255,255,0.06); }
  .statement-title {
    font-family: "Saira Condensed", "Arial Narrow", sans-serif; font-weight: 600;
    font-size: 24px; line-height: 29px;
  }
  .statement-body { font-size: 11px; line-height: 15.2px; margin-top: 6px; }
  .statement-body.large { font-size: 14.6px; line-height: 16.5px; margin-top: 6px; }
  .statement-body + .statement-body { margin-top: 16px; }
  .value-list { margin-bottom: 12px; }
  .poster-footer { height: 35px; background: var(--footer); }
</style>
</head>
<body>
  <main class="poster">
    <header class="brand-bar">
      <span class="brand-mark"></span>
      <span class="brand-name">CareWillow</span>
    </header>

    <section class="hero">
      <div class="hero-photo" role="img" aria-label="Portrait of a smiling professional in a dark suit and striped tie against a grey wall"></div>
      <div class="hero-message">
        <h1 class="hero-headline">We consistently deliver what we promise, and whenever possible,</h1>
        <p class="hero-copy">Clients choose us, and develop lasting bonds with our team because of our impeccably high standards and our reputation for always remembering this is, first and foremost, a people business.</p>
      </div>
    </section>

    <section class="promise-band">
      <p>We consistently go the extra mile to ensure our nurses and those being cared for are at all times, treated with dignity and respect. We hold ourselves and those we work with to the highest possible standards.</p>
    </section>

    <section class="statement-grid">
      <article class="statement">
        <h2 class="statement-title">Our Values:</h2>
        <p class="statement-body">Through our genuine caring and compassion, we are committed to honor all with whom we interact. We are grounded in our faith and dedicated to working together as a family that consistently and passionately lives our values. Compassion Integrity and honesty Faith Decisive action Constant and never-ending improvement</p>
      </article>
      <article class="statement right">
        <h2 class="statement-title">Our Vision Statement:.</h2>
        <p class="statement-body large">We are transforming the healthcare staffing and homecare industry with our people-oriented, world-class team.</p>
      </article>
      <article class="statement lower">
        <h2 class="statement-title value-list">Personal ownership Excellence Positive attitude Passion Respect Who we are:</h2>
        <p class="statement-body">We are friendly, servant leaders who have a sense of urgency to meet the needs of our nurses and clients. We prioritize personal relationships with genuine caring and compassion. We inspire others through our passion and energy.</p>
      </article>
      <article class="statement right lower">
        <h2 class="statement-title">Our Mission Statement:</h2>
        <p class="statement-body large">We go above and beyond to ensure our clients receive the right care and the right people at the right time.</p>
        <p class="statement-body large">Our rigorous recruitment standards result in strong caregivers who are trusted for their expertise, experience and compassion.</p>
      </article>
    </section>

    <footer class="poster-footer"></footer>
  </main>
</body>
</html>
```